Create a Business Card Design Project for a new logistics company

We need a business card designed for a new company in Australia.

Type of business is logistics/trucking.

Medium will be brushed black metal card that can/will be acid etched to a brushed steel silver, acid die cut and two printed colours of our choice which will be white and pantone orange.

We have hopes that the design will be simple, modern and represent with a quick glance what our company does.

Please read instructions carefully in must have box any questions please ask.

If you are interested in this job please look at other job that we have which is very similar with logo and design

Please have a look at the things that can be done with metals cards on google images for inspiration.

Target Market(s)

Men from 20yrs of age to 60yrs of age

Industry/Entity Type

Steel

Requirements
Must have
• Must Have:
- Front of card:

Must use the company logo and name provided as attachment (see below KWR-black-background-cmyk).
Logo grey will be etched, orange and white will be printed on card. Parts of the logo could even be die cut.

The word -Logistics anytime, anywhere- on front etched, printed or die cut.

detail needed on front or back depending on your design layout.

Name
position
email
mobile

all details can be on front if a nice design is etched on the back of card or to keep front simple you can put all detail on back of card, I will leave the lay out to you.

Colours in logo are

Pantone 144 C Orange
Pantone 11-0601 White
Pantone 7539 C Gray
Pantone 426 C Black

However black will be the base of black metal card. Gray will be replaced with the etching in card revealing the silver. Orange and white will be printed on card.

have fun!!
Nice to have
• The file attached called idea is just an example of what can be designed and etched into card. Google has many more idea's for metal business cards.
Should not have
• Please don't clutter the card
No fonts smaller then 7 points

```html
<!DOCTYPE html>
<html lang="en">
<head>
<meta charset="utf-8">
<title>KWR Industries – Business Card</title>
<link href="https://fonts.googleapis.com/css2?family=Arimo:wght@400;700&display=swap" rel="stylesheet">
<style>
  :root {
    --page: #ffffff;
    --card-dark: #161616;
    --card-mid: #2a2a2a;
    --lane-white: #bdbdbd;
    --print-white: #ffffff;
    --print-orange: #e8641c;
    --etch-grey: #9b9b9b;
  }
  html, body {
    margin: 0;
    padding: 0;
    width: 1200px;
    height: 1000px;
    overflow: hidden;
    background: var(--page);
    font-family: "Arimo", Arial, sans-serif;
  }
  .canvas {
    position: relative;
    width: 1200px;
    height: 1000px;
  }
  .card-shape {
    position: absolute;
    left: 0;
    top: 0;
  }
  .brand-name {
    position: absolute;
    left: 400px;
    top: 288px;
    margin: 0;
    font-size: 58px;
    font-weight: 700;
    letter-spacing: 2px;
    line-height: 1;
    color: var(--print-orange);
  }
  .holder {
    position: absolute;
    left: 148px;
    width: 902px;
    top: 490px;
    text-align: center;
    color: var(--print-white);
  }
  .holder-name {
    margin: 0;
    font-size: 56px;
    font-weight: 700;
    line-height: 1.05;
    letter-spacing: 0.5px;
  }
  .holder-role {
    margin: 4px 0 0;
    font-size: 27px;
    font-weight: 700;
    line-height: 1.1;
  }
  .contacts {
    position: absolute;
    left: 148px;
    width: 902px;
    top: 644px;
    display: flex;
    justify-content: center;
    align-items: center;
    gap: 30px;
    color: var(--print-white);
    font-size: 26px;
    font-weight: 400;
  }
  .contact-item {
    display: flex;
    align-items: center;
    gap: 8px;
  }
  .contact-item svg { display: block; }
</style>
</head>
<body>
<div class="canvas">
  <svg class="card-shape" width="1200" height="1000" viewBox="0 0 1200 1000" aria-hidden="false">
    <defs>
      <linearGradient id="asphalt" x1="0" y1="0" x2="0" y2="1">
        <stop offset="0" stop-color="#141414"/>
        <stop offset="0.45" stop-color="#262626"/>
        <stop offset="1" stop-color="#1e1e1e"/>
      </linearGradient>
      <clipPath id="cardClip">
        <path d="M148,297 H210 V252 Q210,232 230,232 H352 Q378,232 386,256 L392,272 H965 Q985,272 985,290 V297 H1050 V736 H148 Z"/>
      </clipPath>
    </defs>
    <g clip-path="url(#cardClip)">
      <rect class="card-surface" x="140" y="225" width="920" height="520" fill="url(#asphalt)" role="img" aria-label="Asphalt road surface texture"/>
      <g class="lane-dashes" fill="var(--lane-white)" opacity="0.8">
        <rect x="148" y="447" width="105" height="21"/>
        <rect x="349" y="447" width="105" height="21"/>
        <rect x="548" y="447" width="105" height="21"/>
        <rect x="748" y="447" width="105" height="21"/>
        <rect x="948" y="447" width="102" height="21"/>
      </g>
      <rect class="edge-line" x="148" y="700" width="902" height="22" fill="var(--print-orange)"/>
    </g>
    <circle class="brand-dot" cx="296" cy="314" r="62" fill="var(--etch-grey)"/>
  </svg>

  <p class="brand-name">KWR INDUSTRIES</p>

  <div class="holder">
    <h1 class="holder-name">LIAM CORVELL</h1>
    <p class="holder-role">Digital Creative Director</p>
  </div>

  <div class="contacts">
    <span class="contact-item">
      <svg width="40" height="34" viewBox="0 0 40 34" aria-hidden="true">
        <path d="M3,12 Q3,3 20,3 Q37,3 37,12 L37,15 L29,15 L29,10 L11,10 L11,15 L3,15 Z" fill="#fff"/>
        <path d="M12,13 H28 L33,31 H7 Z" fill="#fff"/>
        <g fill="#1e1e1e">
          <rect x="15" y="17" width="2.5" height="2.5"/><rect x="19" y="17" width="2.5" height="2.5"/><rect x="23" y="17" width="2.5" height="2.5"/>
          <rect x="15" y="21" width="2.5" height="2.5"/><rect x="19" y="21" width="2.5" height="2.5"/><rect x="23" y="21" width="2.5" height="2.5"/>
          <rect x="15" y="25" width="2.5" height="2.5"/><rect x="19" y="25" width="2.5" height="2.5"/><rect x="23" y="25" width="2.5" height="2.5"/>
        </g>
      </svg>
      +610-000-0000
    </span>
    <span class="contact-item">
      <svg width="42" height="30" viewBox="0 0 42 30" aria-hidden="true">
        <rect x="1" y="1" width="40" height="28" fill="#fff"/>
        <path d="M1,1 L21,17 L41,1 M1,29 L16,13 M41,29 L26,13" fill="none" stroke="#1e1e1e" stroke-width="1.6"/>
      </svg>
      liam@kwrmail.com
    </span>
  </div>
</div>
</body>
</html>
```